Kestrel Vale is a new and completely innovative health supplement aimed at males between the ages of 25-60.

The supplement is formulated specifically to address two significant factors that affect men as they age. A reduction in the primary sex hormones and a reduction in their fertility.

I already have the logo design and label designed. I am looking to launch the product in January/February following successful trials.
The website won't need to have selling features inbuilt as I will be going through 3rd party platforms.

The website will however need to direct traffic to websites for a couple of purposes. In total I would expect to have in the region of 5-6 pages in total.

```html
<!DOCTYPE html>
<html lang="en">
<head>
<meta charset="utf-8">
<title>Kestrel Vale — Revive Your Vitality</title>
<link href="https://fonts.googleapis.com/css2?family=Barlow:wght@300;400;600;700;800&family=Roboto:wght@400;500;700&display=swap" rel="stylesheet">
<style>
:root{
  --cyan:#14b4ec;
  --ink:#2f2f33;
  --text:#555559;
  --muted:#8a8a90;
  --dark:#444448;
  --footer:#3c3c3e;
  --soft:#f4f5f7;
  --line:#c9ccd2;
  --white:#ffffff;
}
*{box-sizing:border-box;margin:0;padding:0}
html,body{width:1200px;height:3278px;overflow:hidden}
body{font-family:"Roboto",sans-serif;color:var(--text);background:var(--white);position:relative}
.abs{position:absolute}
.heading{font-family:"Barlow",sans-serif;font-weight:800;color:var(--ink);letter-spacing:-0.5px}

/* Hero */
.hero{position:absolute;left:0;top:0;width:1200px;height:649px;overflow:hidden}
.hero-photo{position:absolute;inset:0;background:linear-gradient(100deg,#8a5a42 0%,#c89a80 25%,#e9e1dc 45%,#f3f1f0 65%,#eceae8 100%)}
.hero-products{position:absolute;left:735px;top:245px;width:433px;height:404px;background:linear-gradient(90deg,#5b2a17 0%,#7a3a20 35%,#c9a77c 40%,#d8bb92 100%);border-radius:6px 6px 0 0}
.brand-tab{position:absolute;left:30px;top:0;width:130px;height:128px;background:var(--white);border-radius:0 0 60px 60px;display:flex;align-items:center;justify-content:center;text-align:center;font-family:"Barlow",sans-serif;font-weight:800;font-size:22px;line-height:22px;color:var(--cyan)}
.nav{position:absolute;top:32px;right:32px;display:flex;align-items:center;gap:28px;font-size:15px;color:var(--ink)}
.btn{display:inline-flex;align-items:center;justify-content:center;background:var(--cyan);color:var(--white);font-weight:700;border-radius:30px;text-transform:uppercase}
.nav .btn{width:157px;height:47px;font-size:15px;gap:6px;margin-left:4px}
.hero-title{position:absolute;left:580px;top:158px;width:470px;text-align:center;font-family:"Barlow",sans-serif}
.hero-title .bold{font-weight:800;font-size:31px;color:var(--ink);letter-spacing:-0.5px}
.hero-title .light{font-weight:300;font-size:30px;color:var(--cyan);letter-spacing:1px;line-height:32px}

/* Welcome */
.welcome-photo{left:161px;top:715px;width:391px;height:553px;background:linear-gradient(180deg,#b8c9a6 0%,#e6ece5 30%,#f3f4f4 60%,#d6d6d8 100%)}
.welcome{left:590px;top:725px;width:450px;text-align:center}
.pill{display:inline-block;background:var(--cyan);color:var(--white);font-size:14px;letter-spacing:3px;padding:7px 34px;border-radius:20px;font-weight:500}
.welcome h1{font-size:54px;margin-top:12px;line-height:54px}
.tagline{font-size:13px;letter-spacing:10px;color:var(--muted);margin-top:4px}
.welcome p.lead{font-size:12px;line-height:18px;text-align:justify;margin-top:10px}
.features{display:flex;justify-content:space-between;margin-top:20px}
.feature{width:220px}
.icon-circle{width:80px;height:80px;border-radius:50%;background:var(--cyan);margin:0 auto;display:flex;align-items:center;justify-content:center}
.feature h3{font-size:17px;color:var(--ink);font-weight:500;margin-top:18px}
.feature p{font-size:11px;line-height:16px;margin-top:8px}
.stats{display:flex;justify-content:space-between;margin-top:20px}
.stat{width:200px;height:110px;background:var(--soft);border-radius:4px;box-shadow:0 4px 10px rgba(0,0,0,.06);display:flex;flex-direction:column;align-items:center;justify-content:center}
.stat b{font-family:"Barlow",sans-serif;font-size:38px;font-weight:600;color:var(--ink)}
.stat span{font-size:12px;margin-top:6px;color:var(--text)}

/* Service band */
.band{left:0;top:1341px;width:1200px;height:172px;background:var(--dark);display:flex;justify-content:center;gap:0}
.band-item{width:236px;text-align:center;color:var(--white);padding-top:34px}
.band-item h4{font-family:"Roboto",sans-serif;font-size:17px;font-weight:700;margin-top:8px}
.band-item p{font-size:12px;line-height:19px;margin-top:4px}

/* Featured */
.featured-head{left:0;top:1560px;width:1200px;text-align:center}
.featured-head h2{font-size:46px}
.featured-head p{width:740px;margin:14px auto 0;font-size:12px;line-height:19px}
.card{top:1692px;width:284px;text-align:center}
.card .shot{height:375px}
.card h3{font-size:16px;font-weight:500;color:var(--ink);margin-top:18px}
.card p{font-size:12px;line-height:18px;margin-top:8px}
.card .btn{width:135px;height:44px;font-size:12px;margin-top:20px}

/* Contact */
.touch{left:0;top:2298px;width:1200px;height:547px;background:linear-gradient(180deg,#f2f4f7,#e9edf2)}
.touch h2{font-size:54px;text-align:center;margin-top:52px}
.touch .sub{text-align:center;font-size:14px;margin-top:4px}
.field{position:absolute;background:var(--white);border:1px solid var(--line);font-size:11px;color:var(--muted);padding:0 15px;display:flex;align-items:center}
.field.area{align-items:flex-start;padding-top:18px}
.touch .btn{position:absolute;left:503px;top:431px;width:188px;height:56px;font-size:16px}

/* Footer */
.footer{left:0;top:2845px;width:1200px;height:358px;background:var(--footer);color:#e6e6e6}
.info-box{position:absolute;top:42px;width:270px;height:71px;border:1px solid #6b6b6e;display:flex;align-items:center;font-size:12px;line-height:17px}
.info-box .ico{width:38px;height:53px;background:#e9e9ea;margin:0 12px 0 0;display:flex;align-items:center;justify-content:center}
.footer h5{position:absolute;top:152px;font-size:18px;font-weight:500;color:var(--white)}
.about-text{position:absolute;left:162px;top:185px;width:265px;font-size:11px;line-height:17px}
.read-more{position:absolute;left:162px;top:262px;font-size:10px}
.social{position:absolute;left:162px;top:290px;display:flex;gap:10px}
.social span{width:27px;height:27px;border-radius:50%;background:#e6e6e6}
.links{position:absolute;left:560px;top:188px;list-style:none;font-size:12px;line-height:25.5px}
.links li::before{content:"» ";font-size:10px}
.news-input{position:absolute;left:836px;top:188px;width:200px;height:43px;background:#ececec;color:#777;font-size:10px;padding:0 15px;display:flex;align-items:center}
.footer .btn{position:absolute;left:836px;top:246px;width:120px;height:38px;font-size:13px}
.copyright{left:0;top:3203px;width:1200px;height:75px;background:var(--cyan);color:var(--white);font-size:12px;display:flex;align-items:center;justify-content:center}
</style>
</head>
<body>

<header class="hero">
  <div class="hero-photo" role="img" aria-label="Smiling couple embracing in a bright kitchen"></div>
  <div class="hero-products" role="img" aria-label="Amber multivitamin bottle beside its kraft paper box"></div>
  <div class="brand-tab">Kestrel<br>Vale</div>
  <nav class="nav">
    <span>HOME</span><span>ABOUT US</span><span>PRODUCTS</span>
    <span class="btn">
      <svg width="15" height="12" viewBox="0 0 15 12" fill="none" stroke="#fff" stroke-width="1.5"><rect x="1" y="1" width="13" height="10"/><path d="M1 1l6.5 5.5L14 1"/></svg>
      Contact us
    </span>
  </nav>
  <div class="hero-title">
    <div class="bold">ADVANCED MULTI-COMPLEX</div>
    <div class="light">FORMULA FOR MEN</div>
  </div>
</header>

<div class="abs welcome-photo" role="img" aria-label="White supplement jar on a wooden table"></div>
<section class="abs welcome">
  <span class="pill">WELCOME TO</span>
  <h1 class="heading">KESTREL VALE</h1>
  <div class="tagline">REVIVE YOUR VITALITY</div>
  <p class="lead">Lorem Ipsum is simply dummy text of the printing and typesetting industry. Lorem Ipsum has been the industry's standard dummy text ever since the 1500s, when an unknown printer took a galley of type and scrambled it to make a type specimen book. It has survived not only five centuries, but also the leap into electronic typesetting, remaining essentially unchanged. It was popularised in the 1960s with the release of Letraset sheets containing Lorem Ipsum passages, and more recently</p>
  <div class="features">
    <div class="feature">
      <div class="icon-circle"><svg width="42" height="42" viewBox="0 0 42 42" fill="none" stroke="#fff" stroke-width="2"><rect x="8" y="6" width="22" height="30" rx="2"/><rect x="14" y="3" width="10" height="6" rx="1"/><path d="M13 16h12M13 22h8M13 28h6"/><circle cx="31" cy="30" r="6"/></svg></div>
      <h3>Health Supplement</h3>
      <p>Lorem Ipsum is simply dummy text Ipsum has been the industry's standard an scrambled it to make specimen book.</p>
    </div>
    <div class="feature">
      <div class="icon-circle"><svg width="44" height="44" viewBox="0 0 44 44" fill="none" stroke="#fff" stroke-width="2"><path d="M22 8l7 4v8l-7 4-7-4v-8zM15 20l-7 4v8l7 4 7-4v-8M29 20l7 4v8l-7 4-7-4"/></svg></div>
      <h3>Sex Hormones</h3>
      <p>Lorem Ipsum is simply dummy text Ipsum has been the industry's standard an scrambled it to make specimen book.</p>
    </div>
  </div>
  <div class="stats">
    <div class="stat"><b>180+</b><span>CAPSULES FOOD SUPPLEMENT</span></div>
    <div class="stat"><b>129+</b><span>OUR EXPERT TEAM</span></div>
  </div>
</section>

<section class="abs band">
  <div class="band-item">
    <svg width="38" height="38" viewBox="0 0 38 38" fill="none" stroke="#fff" stroke-width="2"><circle cx="19" cy="19" r="16"/><text x="19" y="23" font-size="11" font-weight="700" fill="#fff" stroke="none" text-anchor="middle" font-family="Roboto,sans-serif">24</text></svg>
    <h4>24/7 SERVICE</h4><p>Lorem Ipsum is simply dummy text printing industry.</p>
  </div>
  <div class="band-item">
    <svg width="38" height="38" viewBox="0 0 38 38" fill="#fff"><circle cx="19" cy="11" r="7"/><path d="M5 36c0-9 6-15 14-15s14 6 14 15z"/></svg>
    <h4>PROFESSIONAL</h4><p>Lorem Ipsum is simply dummy text printing industry.</p>
  </div>
  <div class="band-item">
    <svg width="38" height="38" viewBox="0 0 38 38" fill="none" stroke="#fff" stroke-width="2"><circle cx="21" cy="12" r="8"/><path d="M4 30l8-5h10l8-4M4 36h14l14-8"/></svg>
    <h4>AFFORDABLE</h4><p>Lorem Ipsum is simply dummy text printing industry.</p>
  </div>
  <div class="band-item">
    <svg width="38" height="38" viewBox="0 0 38 38" fill="none" stroke="#fff" stroke-width="2.5"><circle cx="19" cy="19" r="13"/><path d="M13 19l5 5 8-9"/></svg>
    <h4>GUARANTEED</h4><p>Lorem Ipsum is simply dummy text printing industry.</p>
  </div>
</section>

<section class="abs featured-head">
  <h2 class="heading">FEATURED PRODUCTS</h2>
  <p>Lorem Ipsum is simply dummy text of the printing and typesetting industry lorem Ipsum has been the industry's standard dummy text ever has survived Letraset sheets containing Lorem Ipsum passages desktop PageMaker including versions of Lorem Ipsum.</p>
</section>

<article class="abs card" style="left:161px">
  <div class="shot" role="img" aria-label="Two protein powder tubs with a green apple" style="background:linear-gradient(180deg,#3f7a66,#1f2a28)"></div>
  <h3>Lorem Ipsum is simply text</h3>
  <p>Lorem Ipsum is simply dummy text of the printing survived not only five centuries, but also the leap into passages, and more recently with desktop publishing software pagemaker including Lorem Ipsum.</p>
  <span class="btn">View details</span>
</article>
<article class="abs card" style="left:457px">
  <div class="shot" role="img" aria-label="Vitamin bottle surrounded by colourful mineral spheres" style="background:linear-gradient(180deg,#5ec3ee,#c9ecfa 55%,#8fd4f2)"></div>
  <h3>Lorem Ipsum is simply text</h3>
  <p>Lorem Ipsum is simply dummy text of the printing survived not only five centuries, but also the leap into passages, and more recently with desktop publishing software pagemaker including Lorem Ipsum.</p>
  <span class="btn">View details</span>
</article>
<article class="abs card" style="left:754px">
  <div class="shot" role="img" aria-label="Vitamin complex bottle with orange vitamin capsules on turquoise" style="background:linear-gradient(180deg,#1ad2d6,#7ee8e4 55%,#18b9bd)"></div>
  <h3>Lorem Ipsum is simply text</h3>
  <p>Lorem Ipsum is simply dummy text of the printing survived not only five centuries, but also the leap into passages, and more recently with desktop publishing software pagemaker including Lorem Ipsum.</p>
  <span class="btn">View details</span>
</article>

<section class="abs touch">
  <h2 class="heading">GET IN TOUCH</h2>
  <p class="sub">Your request will be answered withing 24 hours</p>
  <div class="field" style="left:265px;top:162px;width:326px;height:50px">Enter your name</div>
  <div class="field" style="left:602px;top:162px;width:340px;height:50px">Enter your phone</div>
  <div class="field" style="left:265px;top:223px;width:326px;height:50px">Enter your email</div>
  <div class="field" style="left:602px;top:223px;width:340px;height:50px">Enter your address</div>
  <div class="field area" style="left:265px;top:284px;width:678px;height:124px">Enter your comments</div>
  <span class="btn">Send message</span>
</section>

<footer class="abs footer">
  <div class="info-box" style="left:162px">
    <span class="ico"><svg width="16" height="20" viewBox="0 0 16 20" fill="none" stroke="#777" stroke-width="1.4"><path d="M8 19s6-6.5 6-11A6 6 0 002 8c0 4.5 6 11 6 11z"/><circle cx="8" cy="8" r="2.2"/></svg></span>
    Lorem Ipsum is simply dummy text<br>printing and typesetting industry
  </div>
  <div class="info-box" style="left:471px">
    <span class="ico"><svg width="20" height="20" viewBox="0 0 20 20" fill="none" stroke="#777" stroke-width="1.4"><path d="M4 2l4 4-2 3c1 2 3 4 5 5l3-2 4 4-3 3C8 18 2 12 1 5z"/></svg></span>
    Phone: 555.204.3187<br>Fax: 555.204.3190
  </div>
  <div class="info-box" style="left:769px">
    <span class="ico"><svg width="20" height="16" viewBox="0 0 20 16" fill="none" stroke="#777" stroke-width="1.4"><rect x="1" y="1" width="18" height="14"/><path d="M1 1l9 7 9-7"/></svg></span>
    info@kestrelvale.com
  </div>

  <h5 style="left:162px">ABOUT US</h5>
  <p class="about-text">Lorem Ipsum is simply dummy text of the printing and typesetting industry. Lorem Ipsum has been the industry's unknown printer took a galley of type and scrambled it to make a type specimen book.</p>
  <span class="read-more">Read More »</span>
  <div class="social"><span></span><span></span><span></span><span></span></div>

  <h5 style="left:560px">INFORMATION</h5>
  <ul class="links">
    <li>Home</li><li>About us</li><li>Products</li><li>Contact us</li><li>Terms &amp; Conditions</li><li>Privacy Policy</li>
  </ul>

  <h5 style="left:836px">NEWSLETTER</h5>
  <div class="news-input">Enter Your Email Id</div>
  <span class="btn">Subscribe</span>
</footer>

<div class="abs copyright">Copyright 2023 kestrelvale.com. All Right Reserved.</div>

</body>
</html>
```